Business card layouts, letter head, brochures envelops
Maple Harbor Outdoor Works Group Project
Bright & Fun-filled
Peter Halvik
We have multiple locations:
1) 27583 NE Parkway Suite #415-309
Sugar Land, Texas 77590
2) 8342 Corvina Alta Dr.
The Villages, Florida 32999
281-555-0147 Texas Lakeview, Florida 407-555-0193
peter@maplehavenyardworksolutions.example
maplehavenyardworksservicesgroup.example
Licensed , Insured, Bonded
Your single source service provider !
Lawn Care, Fertilization, Pest & Termite Elimination, Landscape Management , Landscape Installations, Sprinkler System Installations, Lot Sweeping, Tree & Shrub Care, Mosquito Control, Grease Trap Cleaning, Septic System Cleaning & Installations , Full service Plumbing and Drain Cleaning

```html
<!DOCTYPE html>
<html lang="en">
<head>
<meta charset="utf-8">
<title>Maple Harbor Outdoor Works Group – Stationery Set</title>
<link href="https://fonts.googleapis.com/css2?family=Open+Sans:wght@400;700;800&display=swap" rel="stylesheet">
<style>
  :root{
    --bg:#1f3a22;
    --bg-dark:#142816;
    --green:#3fae1c;
    --green-bright:#58c922;
    --green-deep:#207a10;
    --black:#0c0c0c;
    --white:#ffffff;
    --paper:#fbfbf8;
    --grey:#6b6b6b;
    --faint:#e6eddc;
  }
  *{box-sizing:border-box;margin:0;padding:0}
  html,body{width:1200px;height:423px;overflow:hidden}
  body{
    background:radial-gradient(ellipse at 50% 50%,var(--bg) 0%,var(--bg-dark) 100%);
    font-family:"Open Sans",Arial,sans-serif;
    position:relative;
  }
  .item{position:absolute;box-shadow:0 3px 8px rgba(0,0,0,.55);overflow:hidden}

  .brand{font-weight:800;color:var(--green-bright);letter-spacing:.3px;display:flex;align-items:center;gap:4px;white-space:nowrap}
  .brand .dot{display:inline-block;border-radius:50%;background:var(--green-bright)}

  /* business cards */
  .card{left:24px;width:150px;height:86px}
  .card--front{top:67px;background:var(--white)}
  .card--front .band{position:absolute;inset:0 0 auto 0;height:36px}
  .card--front .name{position:absolute;left:6px;top:6px;font-size:5px;font-weight:700;color:var(--white)}
  .card--front .brand{position:absolute;left:58px;top:8px;font-size:8px}
  .card--front .brand .dot{width:5px;height:5px}
  .card--front .info{position:absolute;left:58px;top:20px;font-size:3.4px;line-height:4.4px;color:var(--white)}
  .card--front .foot{position:absolute;left:6px;right:6px;bottom:6px;font-size:3.4px;line-height:4.4px;color:var(--grey)}

  .card--services{top:175px;background:var(--black);padding:6px 7px}
  .card--services h3{font-size:4.6px;color:var(--green-bright);font-weight:700;margin-bottom:3px}
  .card--services ul{list-style:none;columns:2;column-gap:8px;font-size:3.6px;line-height:5px;color:var(--green-bright)}
  .card--services .tag{position:absolute;left:0;right:0;bottom:5px;text-align:center;font-size:3.6px;color:var(--white)}

  .card--back{top:276px;background:linear-gradient(180deg,var(--green-bright),var(--green-deep));padding:8px 7px}
  .card--back h3{font-size:4.6px;color:var(--white);font-weight:700;margin-bottom:3px}
  .card--back p{font-size:3.6px;line-height:5px;color:var(--white)}

  /* letterheads */
  .letterhead{top:24px;width:271px;height:379px;background:var(--paper)}
  .letterhead--one{left:221px}
  .letterhead--two{left:514px}
  .letterhead .header{position:absolute;inset:0 0 auto 0;height:70px}
  .letterhead .brand{position:absolute;left:24px;top:18px;font-size:12px}
  .letterhead .brand .dot{width:9px;height:9px}
  .letterhead .contact{position:absolute;left:142px;top:10px;font-size:3.8px;line-height:5px;color:var(--white)}
  .letterhead .mark{position:absolute;left:70px;top:135px;width:130px;height:110px;border-radius:50%;
    background:radial-gradient(circle,var(--faint) 0%,rgba(230,237,220,0) 70%)}
  .letterhead .footer{position:absolute;left:22px;right:22px;bottom:12px;font-size:3.6px;line-height:4.8px;color:var(--grey);text-align:center}
  .letterhead--one .footer{text-align:left}

  /* envelopes */
  .envelope{background:var(--white)}
  .envelope--flap{left:816px;top:36px;width:360px;height:120px}
  .envelope--green{left:845px;top:91px;width:336px;height:99px}
  .envelope--plain{left:822px;top:175px;width:348px;height:113px}
  .envelope--dark{left:811px;top:250px;width:305px;height:134px}
  .envelope svg{position:absolute;inset:0}
  .envelope .seal{position:absolute;left:50%;top:38px;width:14px;height:14px;margin-left:-7px;border-radius:50%;background:var(--green)}
  .envelope--green .brand{position:absolute;left:50%;transform:translateX(-50%);top:10px;font-size:8px;color:var(--white)}
  .envelope--green .brand .dot{width:5px;height:5px;background:var(--white)}
  .envelope--dark .brand{position:absolute;left:12px;top:10px;font-size:9px}
  .envelope--dark .brand .dot{width:6px;height:6px}
  .envelope--dark .return{position:absolute;left:12px;top:24px;font-size:3.8px;line-height:5px;color:var(--white)}
  .envelope--dark .mark{position:absolute;left:110px;top:60px;width:90px;height:60px;border-radius:50%;
    background:radial-gradient(circle,var(--faint) 0%,rgba(230,237,220,0) 70%)}
</style>
</head>
<body>

<section class="item card card--front">
  <svg class="band" width="150" height="36" viewBox="0 0 150 36">
    <path d="M0 0H150V26Q75 40 0 30Z" fill="var(--black)"/>
    <path d="M0 30Q75 40 150 26V29Q75 44 0 33Z" fill="var(--green)"/>
  </svg>
  <div class="name">Peter Halvik</div>
  <div class="brand"><span class="dot"></span>Maple Haven</div>
  <div class="info">Maple Harbor Outdoor Works Group</div>
  <div class="foot">
    27583 NE Parkway Suite #200, Brookfield Bend, Texas 77590<br>
    8342 Corvina Alta Dr., Palm Crest, Florida 32999<br>
    281-555-0147 · 407-555-0193<br>
    peter@maplehavenyardworksolutions.example
  </div>
</section>

<section class="item card card--services">
  <h3>Your single source service provider !</h3>
  <ul>
    <li>Lawn Care</li><li>Fertilization</li><li>Pest &amp; Termite Elimination</li>
    <li>Landscape Management</li><li>Landscape Installations</li><li>Sprinkler System Installations</li>
    <li>Lot Sweeping</li><li>Tree &amp; Shrub Care</li><li>Mosquito Control</li>
    <li>Grease Trap Cleaning</li><li>Septic System Cleaning</li><li>Plumbing &amp; Drain Cleaning</li>
  </ul>
  <div class="tag">Licensed, Insured, Bonded</div>
</section>

<section class="item card card--back">
  <h3>We have multiple locations:</h3>
  <p>1) 27583 NE Parkway Suite #200, Brookfield Bend, Texas 77590<br>
     2) 8342 Corvina Alta Dr., Palm Crest, Florida 32999<br>
     Texas 281-555-0147 · Lakeview, Florida 407-555-0193<br>
     maplehavenyardworksservicesgroup.example</p>
</section>

<section class="item letterhead letterhead--one">
  <svg class="header" width="271" height="70" viewBox="0 0 271 70">
    <path d="M0 0H271V50Q150 74 0 52Z" fill="var(--black)"/>
    <path d="M0 52Q150 74 271 50V55Q150 80 0 57Z" fill="var(--green)"/>
  </svg>
  <div class="brand"><span class="dot"></span>Maple Haven</div>
  <div class="contact">
    27583 NE Parkway Suite #200<br>Brookfield Bend, Texas 77590<br>
    8342 Corvina Alta Dr.<br>Palm Crest, Florida 32999<br>
    281-555-0147 · 407-555-0193
  </div>
  <div class="mark" role="img" aria-label="Faint landscape emblem watermark"></div>
  <div class="footer">maplehavenyardworksservicesgroup.example</div>
</section>

<section class="item letterhead letterhead--two">
  <svg class="header" width="271" height="70" viewBox="0 0 271 70">
    <path d="M0 0H271V50Q150 74 0 52Z" fill="var(--black)"/>
    <path d="M0 52Q150 74 271 50V55Q150 80 0 57Z" fill="var(--green)"/>
  </svg>
  <div class="brand"><span class="dot"></span>Maple Haven</div>
  <div class="mark" role="img" aria-label="Faint landscape emblem watermark"></div>
  <div class="footer">
    27583 NE Parkway Suite #200, Brookfield Bend, Texas 77590 · 281-555-0147<br>
    8342 Corvina Alta Dr., Palm Crest, Florida 32999 · 407-555-0193<br>
    peter@maplehavenyardworksolutions.example · Licensed, Insured, Bonded
  </div>
</section>

<section class="item envelope envelope--flap">
  <svg width="360" height="120" viewBox="0 0 360 120">
    <path d="M0 0L180 70L360 0" fill="none" stroke="#d8d8d8" stroke-width="1"/>
  </svg>
  <div class="seal"></div>
</section>

<section class="item envelope envelope--green">
  <svg width="336" height="99" viewBox="0 0 336 99">
    <path d="M0 0H336L168 48Z" fill="var(--green)"/>
    <path d="M0 0L168 48L336 0" fill="none" stroke="var(--green-deep)" stroke-width="1"/>
  </svg>
  <div class="brand"><span class="dot"></span>Maple Haven</div>
</section>

<section class="item envelope envelope--plain">
  <svg width="348" height="113" viewBox="0 0 348 113">
    <path d="M0 0L174 55L348 0" fill="none" stroke="#d8d8d8" stroke-width="1"/>
  </svg>
</section>

<section class="item envelope envelope--dark">
  <svg width="305" height="134" viewBox="0 0 305 134">
    <path d="M0 0H305V44Q160 66 0 48Z" fill="var(--black)"/>
    <path d="M0 48Q160 66 305 44V48Q160 71 0 52Z" fill="var(--green)"/>
  </svg>
  <div class="brand"><span class="dot"></span>Maple Haven</div>
  <div class="return">27583 NE Parkway Suite #200<br>Brookfield Bend, Texas 77590</div>
  <div class="mark" role="img" aria-label="Faint landscape emblem watermark"></div>
</section>

</body>
</html>
```